KT-Systems advertising flag and billboard design

I need a design for advertising flag and a design for billboard.
Information can be obtained from https://kt-sytronik.de.
Updates
Target Market(s)
IT service for companies
Requirements
Must have
- Logo, contact information and services

```html
<!DOCTYPE html>
<html lang="de">
<head>
<meta charset="utf-8">
<title>KT-Systems – Billboard und Werbeflaggen</title>
<link href="https://fonts.googleapis.com/css2?family=Montserrat:wght@500;600;700;800&display=swap" rel="stylesheet">
<style>
  :root{
    --navy-deep:#050a2e;
    --navy:#0b1450;
    --blue:#1e2fd6;
    --blue-bright:#3a4cff;
    --cyan:#7fb6ff;
    --white:#ffffff;
    --stage:#eef0f4;
  }
  *{margin:0;padding:0;box-sizing:border-box}
  html,body{width:675px;height:1200px;overflow:hidden}
  body{background:var(--stage);font-family:"Montserrat",sans-serif;color:var(--white);position:relative}

  .billboard{position:absolute;left:30px;top:60px;width:615px;height:380px;border-radius:4px;overflow:hidden;
    background:radial-gradient(ellipse at 75% 35%,#14207a 0%,var(--navy) 40%,var(--navy-deep) 100%);}
  .billboard__texture{position:absolute;inset:0;background:linear-gradient(160deg,rgba(60,90,255,.12),rgba(0,0,0,0) 60%)}
  .billboard__band{position:absolute;left:0;right:0;bottom:0;height:54px;
    background:linear-gradient(90deg,var(--blue) 0%,var(--blue-bright) 60%,var(--blue) 100%)}
  .billboard__band::before{content:"";position:absolute;left:0;right:0;top:-8px;height:4px;background:var(--blue-bright);opacity:.6}

  .brand{position:absolute;right:28px;top:26px;display:flex;align-items:center;gap:8px}
  .brand__dot{width:34px;height:34px;border-radius:50%;background:var(--blue-bright)}
  .brand__name{font-weight:800;font-size:20px;color:var(--white)}

  .headline{position:absolute;left:34px;top:58px}
  .headline__lead{font-size:24px;font-weight:600}
  .headline__main{font-size:60px;font-weight:800;line-height:1;margin-top:2px;letter-spacing:-1px}

  .services{position:absolute;left:34px;top:162px;display:grid;grid-template-columns:repeat(2,190px);row-gap:8px;column-gap:20px;font-size:15px;font-weight:600}
  .services li{list-style:none;display:flex;align-items:center;gap:8px}
  .services li::before{content:"";width:7px;height:7px;background:var(--cyan);border-radius:1px}

  .contact-phone{position:absolute;left:34px;top:252px;display:flex;align-items:center;gap:12px;font-size:32px;font-weight:800}
  .contact-phone svg{width:30px;height:30px}
  .contact-lines{position:absolute;left:34px;top:304px;font-size:12px;font-weight:500;display:grid;grid-template-columns:auto auto;column-gap:26px;row-gap:4px}
  .contact-lines span{display:flex;align-items:center;gap:6px}
  .contact-lines svg{width:12px;height:12px}

  .flags{position:absolute;left:0;top:500px;width:675px;height:660px}
</style>
</head>
<body>

<section class="billboard" aria-label="Billboard KT-Systems">
  <div class="billboard__texture" role="img" aria-label="Dunkelblauer Hintergrund mit Platinen-Muster"></div>
  <div class="billboard__band"></div>

  <div class="brand"><span class="brand__dot"></span><span class="brand__name">KT-Systems</span></div>

  <div class="headline">
    <p class="headline__lead">Ihr Partner für</p>
    <h1 class="headline__main">IT-Service</h1>
  </div>

  <ul class="services">
    <li>Firewall-Lösungen</li>
    <li>Antivirensysteme</li>
    <li>Cloud-Lösungen</li>
    <li>E-Mail-Sicherheit</li>
    <li>Hardware Lösungen</li>
    <li>Software Lösungen</li>
  </ul>

  <div class="contact-phone">
    <svg viewBox="0 0 24 24" aria-hidden="true"><path fill="#fff" d="M6.6 10.8a15.1 15.1 0 0 0 6.6 6.6l2.2-2.2c.3-.3.7-.4 1-.2 1.1.4 2.3.6 3.6.6.6 0 1 .4 1 1V20c0 .6-.4 1-1 1A17 17 0 0 1 3 4c0-.6.4-1 1-1h3.5c.6 0 1 .4 1 1 0 1.3.2 2.5.6 3.6.1.3 0 .7-.2 1z"/></svg>
    <span>09952-4417305</span>
  </div>

  <div class="contact-lines">
    <span><svg viewBox="0 0 24 24" aria-hidden="true"><path fill="#fff" d="M12 2a7 7 0 0 0-7 7c0 5 7 13 7 13s7-8 7-13a7 7 0 0 0-7-7zm0 9.5A2.5 2.5 0 1 1 12 6.5a2.5 2.5 0 0 1 0 5z"/></svg>Lindenweg 12, 84100 Talheim</span>
    <span></span>
    <span><svg viewBox="0 0 24 24" aria-hidden="true"><path fill="#fff" d="M3 5h18v14H3zm2 2v.5l7 4.5 7-4.5V7l-7 4.5z"/></svg>info@kt-sytronik.de</span>
    <span><svg viewBox="0 0 24 24" aria-hidden="true"><circle cx="12" cy="12" r="9" fill="none" stroke="#fff" stroke-width="2"/><path d="M3 12h18M12 3c3 3 3 15 0 18M12 3c-3 3-3 15 0 18" fill="none" stroke="#fff" stroke-width="1.5"/></svg>www.kt-sytronik.de</span>
  </div>
</section>

<svg class="flags" viewBox="0 0 675 660" aria-label="Werbeflaggen KT-Systems">
  <defs>
    <linearGradient id="flagFill" x1="0" y1="0" x2="1" y2="1">
      <stop offset="0" stop-color="#0b1450"/>
      <stop offset="1" stop-color="#050a2e"/>
    </linearGradient>
    <linearGradient id="flagSwoosh" x1="0" y1="0" x2="1" y2="0">
      <stop offset="0" stop-color="#1e2fd6"/>
      <stop offset="1" stop-color="#3a4cff"/>
    </linearGradient>
  </defs>

  <g class="flag flag--banner">
    <rect x="175" y="20" width="120" height="600" fill="url(#flagFill)"/>
    <path d="M175 520 C215 500 260 540 295 505 L295 620 L175 620 Z" fill="url(#flagSwoosh)"/>
    <text transform="translate(248 470) rotate(-90)" font-family="Montserrat, sans-serif" font-weight="800" font-size="44" fill="#fff">KT-SYSTEMS</text>
    <text transform="translate(276 430) rotate(-90)" font-family="Montserrat, sans-serif" font-weight="600" font-size="12" fill="#fff">www.kt-sytronik.de</text>
  </g>

  <g class="flag flag--feather">
    <path d="M385 620 L385 60 C385 30 410 20 440 30 C490 50 505 120 505 220 L505 620 Z" fill="url(#flagFill)"/>
    <path d="M385 520 C425 500 470 540 505 505 L505 620 L385 620 Z" fill="url(#flagSwoosh)"/>
    <text transform="translate(456 470) rotate(-90)" font-family="Montserrat, sans-serif" font-weight="800" font-size="42" fill="#fff">KT-SYSTEMS</text>
    <text transform="translate(484 420) rotate(-90)" font-family="Montserrat, sans-serif" font-weight="600" font-size="12" fill="#fff">www.kt-sytronik.de</text>
  </g>
</svg>

</body>
</html>
```